Copperfield Ridge Dental business card

Business card would have following info:

Harold T. Quenneville, DMD, FAGD
General Dentist
email: office@copperfieldridgedental.com
phone: 413-867-3094
fax: 413-867-3094
website: copperfieldridgedental.com

second side would have lines for:

appointment date
appointment time

```html
<!DOCTYPE html>
<html lang="en">
<head>
<meta charset="utf-8">
<title>Copperfield Ridge Dental – Business Card</title>
<link href="https://fonts.googleapis.com/css2?family=Arimo:wght@400;700&display=swap" rel="stylesheet">
<style>
  :root {
    --navy: #0d4a85;
    --sky: #0aa5d6;
    --paper: #ffffff;
    --ink: #2b2b2b;
    --rule: #9a9a9a;
    --backdrop: #e4e4e4;
  }
  * { margin: 0; padding: 0; box-sizing: border-box; }
  html, body { width: 1200px; height: 801px; overflow: hidden; }
  body {
    background: var(--backdrop);
    font-family: "Arimo", Arial, sans-serif;
    position: relative;
  }
  .card {
    position: absolute;
    top: 246px;
    width: 540px;
    height: 309px;
    background: var(--paper);
    overflow: hidden;
    box-shadow: 0 6px 18px rgba(0,0,0,0.18);
  }
  .card--front { left: 40px; }
  .card--back { left: 620px; }
  .card__shapes { position: absolute; inset: 0; }

  /* front */
  .brand-name {
    position: absolute;
    color: var(--navy);
    font-weight: 700;
    font-size: 26px;
    line-height: 1.15;
    text-align: center;
  }
  .card--front .brand-name { left: 330px; top: 62px; width: 200px; }
  .contact { position: absolute; left: 30px; top: 166px; color: var(--paper); }
  .contact__name { color: var(--sky); font-weight: 700; font-size: 16px; }
  .contact__role { font-size: 15px; margin: 3px 0 9px; }
  .contact__list { list-style: none; font-size: 13.5px; line-height: 19px; }
  .contact__list li { display: flex; align-items: center; gap: 7px; }
  .contact__list svg { width: 13px; height: 13px; flex: none; }

  /* back */
  .card--back .brand-name { color: var(--paper); left: 150px; top: 38px; width: 300px; font-size: 28px; }
  .tab-label {
    position: absolute; left: 170px; top: 136px; width: 210px;
    text-align: center; color: var(--paper); font-size: 19px; letter-spacing: 1px;
  }
  .schedule { position: absolute; left: 34px; top: 194px; right: 30px; color: var(--ink); font-size: 16px; }
  .days, .slot { display: flex; align-items: center; }
  .days { gap: 20px; margin-bottom: 22px; }
  .check { display: flex; align-items: center; gap: 8px; }
  .check::before {
    content: ""; width: 13px; height: 13px; border: 2px solid var(--sky);
  }
  .slot { gap: 10px; }
  .slot__line { width: 120px; border-bottom: 1.5px solid var(--ink); height: 14px; margin-right: 14px; }
</style>
</head>
<body>

<section class="card card--front">
  <svg class="card__shapes" viewBox="0 0 540 309" preserveAspectRatio="none" aria-hidden="true">
    <rect width="540" height="309" fill="var(--navy)"/>
    <circle cx="434" cy="46" r="166" fill="var(--sky)"/>
    <circle cx="438" cy="42" r="162" fill="var(--paper)"/>
    <circle cx="442" cy="38" r="156" fill="var(--paper)"/>
  </svg>
  <div class="brand-name">Copperfield Ridge Dental</div>
  <div class="contact">
    <p class="contact__name">Harold T. Quenneville, DMD, FAGD</p>
    <p class="contact__role">General Dentist</p>
    <ul class="contact__list">
      <li><svg viewBox="0 0 16 16"><path fill="var(--sky)" d="M3 1h3l1 4-2 1a9 9 0 0 0 5 5l1-2 4 1v3a2 2 0 0 1-2 2A13 13 0 0 1 1 3a2 2 0 0 1 2-2z"/></svg>413-867-3094</li>
      <li><svg viewBox="0 0 16 16"><path fill="var(--sky)" d="M4 1h8v4H4zM1 6h14v7H1zM4 11h8v4H4z"/></svg>413-867-3094</li>
      <li><svg viewBox="0 0 16 16"><path fill="var(--sky)" d="M1 3h14v10H1z"/><path d="M1 3l7 6 7-6" stroke="var(--navy)" stroke-width="1.5" fill="none"/></svg>office@copperfieldridgedental.com</li>
      <li><svg viewBox="0 0 16 16"><circle cx="8" cy="8" r="7" fill="var(--sky)"/><path d="M1 8h14M8 1c-3 4-3 10 0 14M8 1c3 4 3 10 0 14" stroke="var(--navy)" stroke-width="1" fill="none"/></svg>www.copperfieldridgedental.com</li>
    </ul>
  </div>
</section>

<section class="card card--back">
  <svg class="card__shapes" viewBox="0 0 540 309" preserveAspectRatio="none" aria-hidden="true">
    <rect width="540" height="128" fill="var(--navy)"/>
    <rect y="128" width="540" height="4" fill="var(--sky)"/>
    <polygon points="150,128 410,128 396,162 164,162" fill="var(--sky)"/>
    <line x1="30" y1="180" x2="510" y2="180" stroke="var(--rule)" stroke-dasharray="5 4"/>
  </svg>
  <div class="brand-name">Copperfield Ridge Dental</div>
  <div class="tab-label">APPOINTMENT</div>
  <div class="schedule">
    <div class="days">
      <span class="check">MON</span>
      <span class="check">TUE</span>
      <span class="check">WED</span>
      <span class="check">THU</span>
      <span class="check">FRI</span>
      <span class="check">SAT</span>
    </div>
    <div class="slot">
      <span>DATE</span><span class="slot__line"></span>
      <span>TIME</span><span class="slot__line"></span>
      <span class="check">AM</span>
      <span class="check">PM</span>
    </div>
  </div>
</section>

</body>
</html>
```